vTend Cookbook Cover

I need a design (front and back) for a cookbook cover. Our partners are looking for a few ideas to pick from.
You can see the style for one of the cookbooks we currently carry - uploaded with this brief.
This cookbook is a little different than most cookbooks out there. It is a cancer-fighting cookbook but we don't want it to be so cancer focused that people who don't have cancer will not buy. The book starts out with a section for Foods that Help, then goes to another section called Foods that Hurt. Then, we provide a Recipes section from the ingredients found in Foods that Help. Finally, the last section is called Beyond the Plate and deals with healthy lifestyle habits. You can see a rough draft of the content of the book at the link below. Please keep in mind that the current covers you see are not at all what we want. These were just put there to fill in the space.
Link for cookbook content: https://www.filecrate-share.net/s/4kq29lmzwpbtnxv/The%20Bright%20Bowl%20-%20EDITED.pdf?dl=0
The title: The Bright Bowl
Subtitle: Fighting Cancer One Meal at a Time
Author: Mirel Ostvan
The company that puts the book out is vTend. It would be nice to have the logo somewhere small. Logo can be found here: https://www.filecrate-share.net/s/hrp61wetcozuv3m/vTend%20Logo%20%26%20Guidelines.zip?dl=0
Like "Hand Over A Warmer Day" attached to this brief, we do NOT want something somber but more on the bright side. Just make it look nice and fresh. It would also be nice to somehow incorporate the concept of the cancer ribbon or a silhouette of it in a way that is not upfront but can still be acknowledge. No need for it to be pink and if that does not work, than it's better just to leave it out.
For the back cover, you can design it but simply leave room for us to fill in some text. No need for a spine design as it will be spiral bound.
The file must be designed and saved in PHOTOSHOP format.
According to the designer, the dimensions are:
207mm x 270mm + 5mm bleed
If you want to use the recipe pictures somehow in the cover, just snatch a picture from the content PDF and we can always replace it with the original larger file at a later time. Unfortunately, I don't have the pictures uploaded in filecrate.

```html
<!DOCTYPE html>
<html lang="en">
<head>
<meta charset="utf-8">
<title>The Bright Bowl – cover concepts</title>
<link rel="stylesheet" href="https://fonts.googleapis.com/css2?family=Montserrat:wght@600;700&family=Dosis:wght@500;600&family=Almendra:wght@400&family=Oswald:wght@400&family=Aldrich&display=swap">
<style>
  :root{
    --sheet:#000;
    --paper:#fff;
    --grey-band:rgba(150,150,150,.55);
    --white-band:rgba(255,255,255,.78);
    --pink:#e3186d;
    --yellow:#f6e34a;
    --ink:#2a2a2a;
    --slate:rgba(40,38,40,.86);
    --rule:#c0213f;
    --wood:#3a2c2a;
  }
  html,body{margin:0;padding:0;overflow:hidden;background:var(--sheet);}
  .sheet{position:relative;width:1200px;height:1200px;background:var(--sheet);overflow:hidden;}

  .cover{position:absolute;overflow:hidden;}

  /* ---- Concept A : bright fruit ---- */
  .cover-bright{width:548px;height:720px;}
  .cover-bright .photo{position:absolute;inset:0;
    background:
      radial-gradient(ellipse 45% 40% at 20% 8%, #d8233a 0%, rgba(216,35,58,0) 100%),
      radial-gradient(ellipse 35% 55% at 18% 75%, #7a46a8 0%, rgba(122,70,168,0) 100%),
      radial-gradient(ellipse 60% 50% at 75% 40%, #f7d21a 0%, rgba(247,210,26,0) 100%),
      radial-gradient(ellipse 40% 30% at 60% 80%, #b87a2a 0%, rgba(184,122,42,0) 100%),
      linear-gradient(135deg,#e8ead8 0%,#f3e26a 55%,#f4f0d8 100%);}
  .cover-bright .title-band{position:absolute;left:0;top:180px;width:100%;height:128px;background:var(--grey-band);}
  .cover-bright .title-small{position:absolute;left:82px;top:196px;margin:0;font:700 42px/1 'Montserrat',sans-serif;color:#fff;}
  .cover-bright .title-main{position:absolute;left:26px;top:244px;margin:0;font:700 57px/1 'Montserrat',sans-serif;color:#fff;white-space:nowrap;}
  .cover-bright .ribbon{position:absolute;left:440px;top:160px;width:64px;height:96px;}
  .cover-bright .subtitle-band{position:absolute;left:10px;top:334px;width:540px;height:36px;background:var(--white-band);}
  .cover-bright .subtitle{position:absolute;left:52px;top:337px;margin:0;font:600 25px/30px 'Dosis',sans-serif;color:var(--pink);letter-spacing:.5px;white-space:nowrap;}
  .cover-bright .brand{position:absolute;right:14px;top:26px;display:flex;align-items:center;gap:4px;font:700 22px/1 'Montserrat',sans-serif;color:var(--ink);}
  .cover-bright .brand-dot{width:8px;height:8px;border-radius:50%;background:var(--rule);}
  .cover-bright .author{position:absolute;left:0;width:100%;top:686px;margin:0;text-align:center;font:600 24px/1 'Montserrat',sans-serif;letter-spacing:3px;color:var(--pink);padding-left:40px;box-sizing:border-box;}

  /* ---- Concept B : berry still life ---- */
  .cover-berry{width:546px;height:714px;}
  .cover-berry .photo{position:absolute;inset:0;
    background:
      radial-gradient(ellipse 40% 25% at 55% 65%, #c8202a 0%, rgba(200,32,42,0) 100%),
      radial-gradient(ellipse 60% 30% at 50% 80%, #2d3f6e 0%, rgba(45,63,110,0) 100%),
      radial-gradient(ellipse 40% 40% at 10% 30%, #7d2a4a 0%, rgba(125,42,74,0) 100%),
      radial-gradient(ellipse 40% 40% at 90% 30%, #3e2a5a 0%, rgba(62,42,90,0) 100%),
      linear-gradient(180deg,#5a4a6e 0%,#6a5a88 40%,#2f3c66 75%,#3a2c2a 100%);}
  .cover-berry .frame{position:absolute;left:14px;top:14px;right:14px;bottom:14px;border:2px solid rgba(255,255,255,.35);}
  .cover-berry .title-panel{position:absolute;left:90px;top:86px;width:364px;height:348px;background:var(--slate);border:3px solid rgba(160,160,160,.6);box-sizing:border-box;}
  .cover-berry .title{position:absolute;left:0;top:26px;width:100%;margin:0;text-align:center;font:400 82px/.82 'Almendra',serif;color:#fff;}
  .cover-berry .title span{display:block;}
  .cover-berry .rule{position:absolute;left:12px;right:12px;top:292px;height:2px;background:var(--rule);}
  .cover-berry .subtitle{position:absolute;left:0;width:100%;top:300px;margin:0;text-align:center;font:400 27px/36px 'Oswald',sans-serif;color:#fff;transform:scaleX(.88);}
  .cover-berry .footer{position:absolute;left:14px;right:14px;bottom:14px;height:70px;background:var(--wood);}
  .cover-berry .author{position:absolute;left:140px;top:647px;margin:0;font:400 40px/1 'Aldrich',sans-serif;color:#fff;letter-spacing:1px;}
  .cover-berry .brand{position:absolute;right:34px;top:662px;display:flex;align-items:center;gap:4px;font:400 20px/1 'Aldrich',sans-serif;color:#fff;}
  .cover-berry .brand-dot{width:7px;height:7px;border-radius:50%;background:var(--rule);}

  /* ---- placements ---- */
  .pos-a{left:18px;top:26px;}
  .pos-b{left:634px;top:26px;}
  .preview{position:absolute;background:var(--paper);overflow:hidden;}
  .preview-a{left:113px;top:768px;width:359px;height:403px;}
  .preview-b{left:734px;top:770px;width:357px;height:401px;}
  .preview .cover{left:50%;top:50%;transform-origin:center;}
  .preview-a .cover{margin:-360px 0 0 -274px;transform:scale(.46);box-shadow:0 0 0 1px #ddd;}
  .preview-b .cover{margin:-357px 0 0 -273px;transform:scale(.46);}
</style>
</head>
<body>
<main class="sheet">

  <section class="cover cover-bright pos-a">
    <div class="photo" role="img" aria-label="Close-up photo of red and purple grape clusters against a blurred yellow background"></div>
    <div class="title-band"></div>
    <h1 class="title-small">The</h1>
    <h1 class="title-main">Bright Bowl</h1>
    <div class="ribbon" role="img" aria-label="Yellow awareness ribbon" style="background:radial-gradient(ellipse at center,var(--yellow) 0%,rgba(246,227,74,.5) 60%,rgba(246,227,74,0) 100%);"></div>
    <div class="subtitle-band"></div>
    <p class="subtitle">FIGHTING CANCER ONE MEAL AT A TIME</p>
    <div class="brand"><span class="brand-dot"></span>vTend</div>
    <p class="author">MIREL OSTVAN</p>
  </section>

  <section class="cover cover-berry pos-b">
    <div class="photo" role="img" aria-label="Photo of plums, blueberries, blackberries and red currants on a slate plate over blue denim and dark wood"></div>
    <div class="frame"></div>
    <div class="footer"></div>
    <div class="title-panel">
      <h1 class="title"><span>The</span><span>Bright</span><span>Bowl</span></h1>
      <div class="rule"></div>
      <p class="subtitle">Fighting Cancer One Meal at a Time</p>
    </div>
    <p class="author">Mirel Ostvan</p>
    <div class="brand"><span class="brand-dot"></span>vTend</div>
  </section>

  <div class="preview preview-a">
    <section class="cover cover-bright">
      <div class="photo" role="img" aria-label="Close-up photo of red and purple grape clusters against a blurred yellow background"></div>
      <div class="title-band"></div>
      <p class="title-small">The</p>
      <p class="title-main">Bright Bowl</p>
      <div class="ribbon" role="img" aria-label="Yellow awareness ribbon" style="background:radial-gradient(ellipse at center,var(--yellow) 0%,rgba(246,227,74,.5) 60%,rgba(246,227,74,0) 100%);"></div>
      <div class="subtitle-band"></div>
      <p class="subtitle">FIGHTING CANCER ONE MEAL AT A TIME</p>
      <div class="brand"><span class="brand-dot"></span>vTend</div>
      <p class="author">MIREL OSTVAN</p>
    </section>
  </div>

  <div class="preview preview-b">
    <section class="cover cover-berry">
      <div class="photo" role="img" aria-label="Photo of plums, blueberries, blackberries and red currants on a slate plate over blue denim and dark wood"></div>
      <div class="frame"></div>
      <div class="footer"></div>
      <div class="title-panel">
        <p class="title"><span>The</span><span>Bright</span><span>Bowl</span></p>
        <div class="rule"></div>
        <p class="subtitle">Fighting Cancer One Meal at a Time</p>
      </div>
      <p class="author">Mirel Ostvan</p>
      <div class="brand"><span class="brand-dot"></span>vTend</div>
    </section>
  </div>

</main>
</body>
</html>
```